Awesome Web Design Project

must have a link to palsphere of the homepage preferably a scrolling view of our palsphere page!

We are an exciting new electrical company with a strong focus on energy efficiency and offering the latest technologies.

The design should allow easy navigation, there shouldn't be too many menus, It should look clean and sleek, Colours to consider could be green, silver/chrome, black,

The site should convey technology, efficiency and simplicity

Must be viewable on all devices, pc's, tablets, phones ie Responsive

Logo and some pics uploaded!

Industry/Entity Type

Electrical

Requirements
Must have
• must include the following pages,
about us
our services
gallery
contact us
Connect with us
Nice to have
• Would be great if the website design used a user friendly cms,
Should not have
• too many links, menus, clutter it should be clean and easy to navigate

```html
<!DOCTYPE html>
<html lang="en">
<head>
<meta charset="utf-8">
<title>Voltline Electrical</title>
<link href="https://fonts.googleapis.com/css2?family=Oswald:wght@300;400;500&family=Open+Sans:wght@400;600;700&display=swap" rel="stylesheet">
<style>
:root{
  --lime:#d4dd26;
  --ink:#1d1d1d;
  --nav-text:#3d3d3d;
  --white:#ffffff;
  --panel:#ebebeb;
  --social:#3b5998;
  --arrow-bg:rgba(200,200,200,.55);
  --rule:#d9d9d9;
}
*{margin:0;padding:0;box-sizing:border-box}
html,body{width:1200px;height:900px;overflow:hidden;background:#000}
body{position:relative;font-family:"Open Sans",sans-serif;color:var(--ink)}
.hero{position:absolute;left:0;top:0;width:1200px;height:652px;
  background:radial-gradient(ellipse at 50% 55%,#5a5a5a 0%,#2a2a2a 45%,#0d0d0d 100%)}
.hero-photo{position:absolute;inset:0}
.header{position:absolute;left:16px;top:32px;width:1170px;height:60px;background:var(--white);display:flex;align-items:center}
.brand{display:flex;align-items:center;gap:10px;margin-left:22px;font-family:"Open Sans",sans-serif;font-weight:700;font-size:22px;color:var(--lime);letter-spacing:1px}
.brand-mark{width:28px;height:28px;background:var(--lime)}
.nav{position:absolute;left:483px;top:0;height:60px;display:flex;align-items:center;font-family:"Oswald",sans-serif;font-size:18px;color:var(--nav-text);text-transform:uppercase}
.nav span{position:absolute;white-space:nowrap}
.caret{display:inline-block;margin-left:6px;border:4px solid transparent;border-top:5px solid var(--nav-text);vertical-align:middle}
.connect{position:absolute;left:937px;top:0;width:172px;height:60px;background:var(--lime);font-weight:700;font-size:16px;color:#1e3553;display:flex;align-items:center;justify-content:center}
.social{position:absolute;left:1109px;top:0;width:61px;height:60px;background:var(--social);color:#fff;font-size:10px;font-weight:600;display:flex;align-items:center;justify-content:center}
.arrow{position:absolute;top:343px;width:55px;height:58px;background:var(--arrow-bg);display:flex;align-items:center;justify-content:center}
.arrow.prev{left:0}.arrow.next{right:0}
.headline{position:absolute;top:282px;left:0;width:1200px;text-align:center;font-family:"Oswald",sans-serif;font-weight:400;font-size:66px;color:var(--white);text-transform:uppercase;letter-spacing:-1px}
.headline em{font-style:normal;color:var(--lime)}
.lead{position:absolute;top:374px;left:310px;width:580px;text-align:center;font-family:"Oswald",sans-serif;font-weight:400;font-size:18px;line-height:25px;color:var(--white);text-transform:uppercase;text-shadow:0 1px 2px #000}
.more{position:absolute;left:563px;top:468px;width:81px;height:27px;background:var(--lime);font-family:"Oswald",sans-serif;font-size:15px;color:var(--ink);display:flex;align-items:center;justify-content:center}
.panel{position:absolute;left:0;top:652px;width:1200px;height:248px;background:var(--panel)}
.thumb{position:absolute;width:196px;height:196px;border-radius:50%;border:3px solid var(--white)}
.t1{left:102px;top:537px;background:linear-gradient(160deg,#6e6e6e,#cfcfcf 50%,#4a4a4a)}
.t2{left:499px;top:533px;background:linear-gradient(90deg,#6a4f3a 0%,#c9c9c9 35%,#dedede 70%,#b9b9b9)}
.t3{left:910px;top:533px;background:linear-gradient(180deg,#e0e0e0,#f5f5f5 55%,#a9c8d6)}
.col-title{position:absolute;font-family:"Oswald",sans-serif;font-weight:400;font-size:22px;text-transform:uppercase;color:var(--ink)}
.col-text{position:absolute;width:322px;font-size:13.4px;line-height:20px;text-align:justify;color:#222}
.offer{position:absolute;left:433px;top:790px;width:328px;list-style:none}
.offer li{height:38px;border-bottom:1px solid var(--rule);padding-left:7px;font-size:16px;color:#333;display:flex;align-items:center}
</style>
</head>
<body>
<section class="hero">
  <div class="hero-photo" role="img" aria-label="Row of hanging clear light bulbs against a dark striped wall"></div>
  <div class="arrow prev"><svg width="20" height="28" viewBox="0 0 20 28"><path d="M15 3 5 14l10 11" fill="none" stroke="#222" stroke-width="4"/></svg></div>
  <div class="arrow next"><svg width="20" height="28" viewBox="0 0 20 28"><path d="M5 3l10 11-10 11" fill="none" stroke="#222" stroke-width="4"/></svg></div>
  <h1 class="headline">Innovation <em>Expert</em></h1>
  <p class="lead">Lorem Ipsum is simply dummy text of the printing and typesetting industry. Lorem Ipsum has been the industry's standard dummy text ever since the 1500s,</p>
  <div class="more">MORE</div>
</section>

<header class="header">
  <div class="brand"><span class="brand-mark"></span>VOLTLINE ELECTRICAL</div>
  <nav class="nav">
    <span style="left:0">About Us</span>
    <span style="left:108px">Our Services<i class="caret"></i></span>
    <span style="left:252px">Gallery</span>
    <span style="left:360px">Contact Us</span>
  </nav>
  <div class="connect">CONNECT WITH US</div>
  <div class="social">palsphere</div>
</header>

<section class="panel"></section>
<div class="thumb t1" role="img" aria-label="Living room media wall with television and speakers"></div>
<div class="thumb t2" role="img" aria-label="Ceiling with recessed linear lighting above bookshelves"></div>
<div class="thumb t3" role="img" aria-label="Modern angular LED ceiling light installation"></div>

<h2 class="col-title" style="left:47px;top:754px">Who We Are</h2>
<p class="col-text" style="left:47px;top:808px">Lorem Ipsum is simply dummy text of the printing and typesetting industry. Lorem Ipsum has been the industry's standard dummy text ever since the 1500s, when an unknown printer took a galley of type and scrambled it to make a type specimen book. ook a</p>

<h2 class="col-title" style="left:438px;top:755px">What We Offer</h2>
<ul class="offer">
  <li style="height:36px;margin-top:-2px">Residential / Commercial / Industrial</li>
  <li>Office / Lot Lighting</li>
  <li style="height:32px">Pools / Hot tubs / Spas</li>
</ul>

<h2 class="col-title" style="left:851px;top:726px;font-size:30px;line-height:38px">New</h2>
<h2 class="col-title" style="left:851px;top:760px;font-size:26px">Technologies</h2>
<p class="col-text" style="left:848px;top:811px">Lorem Ipsum is simply dummy text of the printing and typesetting industry. Lorem Ipsum has been the industry's standard dummy text ever since the 1500s, when an unknown printer took a galley of type and scrambled it to make a type specimen book. ook a</p>
</body>
</html>
```